Business Card Design Project for - The Pellowick Greenworks Company Ltd. We are a Landscape and garden

I would like designer to use all special glosses etc so i can have a professional looking business card. The theme of the business card can reflect that of the Logo attached by MarkQuarry or your own unique ideas.. please feel free to go wild as i hope i can select a winner i like - my budget will be committed so please get involved. Good luck and thank you Lyndon

Target Market(s)

Must look Professional

General Public and Businesses including Councils, Local Government, Hospitals, Hotels, Professionals and Professional Sports People.

Industry/Entity Type

Landscape Gardening

Contact Information for Business Card

The Pellowick Greenworks Company Ltd

Mr L.R Ashcombe
Head Office - Quayfront Park Manchester
t. 0772 408 916
e. info@pellowickgreenworks.co.uk
w. www.pellowickgreenworks.co.uk

Facebook - https://www.friendpage-example.com/ThePellowickGreenworksCompany/
Twitter - https://chirpline-example.com/ThePruningCart
Instagram - https://www.snapgrid-example.com/thepellowickgreenworkscompany/?hl=en
Google+ - https://circles.searchhub-example.com/u/0/208473950162438571093
Yelp - https://www.reviewnook-example.co.uk/biz/the-pellowick-greenworks-company-manchester-4

Font styles to use
Serif
Script
Other font styles liked:
• I don't have much of an idea of font types sorry

Colors

Designer to choose colors to be used in the design.

Requirements
Must have
• A Professional look and Design
• Special effects with gloss and fading of colours possibly..
• Front and back design
Nice to have
• All special features with effects and gloss etc

```html
<!DOCTYPE html>
<html lang="en">
<head>
<meta charset="utf-8">
<title>The Pellowick Greenworks Company Ltd — Business Card</title>
<link href="https://fonts.googleapis.com/css2?family=Cinzel:wght@400&family=Dancing+Script:wght@600&family=Open+Sans:wght@400;600&display=swap" rel="stylesheet">
<style>
  :root {
    --page-bg: #d9d9d9;
    --card-black: #1f1d1e;
    --card-black-soft: #2d2a2b;
    --silver-light: #f4f4f4;
    --silver-mid: #cfd0d1;
    --swoosh-grey: #a3a5a7;
    --leaf-green: #3fb63f;
    --script-green: #2fa33a;
    --wordmark-grey: #9a9a9a;
    --text-white: #ffffff;
    --text-dark: #2b2b2b;
    --icon-blue: #3b5998;
    --icon-sky: #39a6e0;
    --icon-pink: #c2347a;
    --icon-red: #d24134;
  }
  * { box-sizing: border-box; margin: 0; padding: 0; }
  html, body { width: 1200px; height: 1200px; overflow: hidden; }
  body {
    background: var(--page-bg);
    font-family: "Open Sans", sans-serif;
    position: relative;
  }
  .card {
    position: absolute;
    left: 250px;
    width: 700px;
    height: 400px;
    border-radius: 34px;
    overflow: hidden;
    box-shadow: 0 10px 30px rgba(0,0,0,0.25);
  }
  /* Back side */
  .card-back {
    top: 130px;
    background: linear-gradient(160deg, var(--card-black-soft), var(--card-black) 60%);
    color: var(--text-white);
  }
  .back-brand {
    position: absolute;
    top: 70px; left: 0; right: 0;
    display: flex; align-items: center; justify-content: center; gap: 14px;
  }
  .brand-dot {
    flex: none;
    width: 46px; height: 46px; border-radius: 50%;
    background: var(--leaf-green);
  }
  .back-brand .brand-name {
    font-family: "Cinzel", serif;
    font-size: 22px;
    color: var(--leaf-green);
    letter-spacing: 1px;
  }
  .social-list {
    position: absolute;
    top: 200px; left: 0; right: 0;
    display: flex; flex-direction: column; align-items: center; gap: 14px;
    font-size: 15px;
    list-style: none;
  }
  .social-row { display: flex; align-items: center; gap: 8px; }
  .social-sep { margin: 0 6px; }
  .social-icon { width: 18px; height: 18px; border-radius: 3px; display: inline-block; }
  .icon-friendpage { background: var(--icon-blue); }
  .icon-chirpline { background: var(--icon-sky); }
  .icon-snapgrid { background: var(--icon-pink); }
  .icon-circles { background: var(--icon-red); }
  .icon-reviewnook { background: var(--icon-red); border-radius: 50%; }

  /* Front side */
  .card-front {
    top: 670px;
    background: linear-gradient(120deg, var(--silver-mid), var(--silver-light) 45%, var(--silver-mid) 75%, var(--silver-light));
  }
  .front-shapes { position: absolute; inset: 0; }
  .front-brand {
    position: absolute;
    left: 50px; top: 160px;
    display: flex; align-items: center; gap: 14px;
  }
  .front-brand .brand-dot { width: 40px; height: 40px; }
  .front-brand .brand-name {
    font-family: "Cinzel", serif;
    color: var(--wordmark-grey);
    font-size: 22px;
    line-height: 1.25;
    letter-spacing: 1px;
  }
  .person {
    position: absolute;
    left: 285px; top: 56px;
    color: var(--text-white);
  }
  .person-name {
    font-family: "Dancing Script", cursive;
    font-weight: 600;
    font-size: 30px;
    line-height: 1.2;
    color: var(--script-green);
    margin-bottom: 4px;
  }
  .person-role, .person-office { font-size: 15px; font-weight: 600; line-height: 1.4; }
  .contact {
    position: absolute;
    right: 40px; bottom: 46px;
    text-align: right;
    color: var(--text-dark);
    font-size: 16px;
    line-height: 1.45;
    list-style: none;
  }
</style>
</head>
<body>
  <section class="card card-back" aria-label="Card back">
    <div class="back-brand">
      <span class="brand-dot"></span>
      <span class="brand-name">The Pellowick Greenworks Company Ltd</span>
    </div>
    <ul class="social-list">
      <li class="social-row"><span class="social-icon icon-friendpage"></span>ThePellowickGreenworksCompany<span class="social-sep">|</span><span class="social-icon icon-chirpline"></span>ThePruningCart</li>
      <li class="social-row"><span class="social-icon icon-snapgrid"></span>thepellowickgreenworkscompany/?hl=en<span class="social-sep">|</span><span class="social-icon icon-circles"></span>208473950162438571093</li>
      <li class="social-row"><span class="social-icon icon-reviewnook"></span>the-pellowick-greenworks-company-manchester-4</li>
    </ul>
  </section>

  <section class="card card-front" aria-label="Card front">
    <svg class="front-shapes" viewBox="0 0 700 400" width="700" height="400" aria-hidden="true">
      <defs>
        <linearGradient id="front-black" x1="0" y1="0" x2="1" y2="1">
          <stop offset="0" stop-color="#2d2a2b"/>
          <stop offset="1" stop-color="#1a1819"/>
        </linearGradient>
      </defs>
      <path d="M0 0 H560 C545 210 390 345 120 400 H0 Z" fill="url(#front-black)"/>
      <path d="M60 372 C330 330 500 220 540 150 C515 250 360 350 100 390 Z" fill="var(--swoosh-grey)"/>
      <path d="M0 345 C250 330 470 240 510 180 C470 270 300 350 40 370 Z" fill="#111" opacity="0.6"/>
    </svg>
    <div class="front-brand">
      <span class="brand-dot"></span>
      <span class="brand-name">The Pellowick<br>Greenworks Company Ltd</span>
    </div>
    <div class="person">
      <p class="person-name">Mr L.R Ashcombe</p>
      <p class="person-role">Head Office</p>
      <p class="person-office">Quayfront Park Manchester</p>
    </div>
    <ul class="contact">
      <li>0772 408 916</li>
      <li>www.pellowickgreenworks.co.uk</li>
      <li>info@pellowickgreenworks.co.uk</li>
    </ul>
  </section>
</body>
</html>
```